Ravenmark Custom goods needs Template Design Love

Our company is called Ravenmark, we offer 1000's of goods, custom printed via silk screen, embroidery, pad printing, and direct print (full color).

Current Project / Need: We are looking for HTML newsletter templates for our customer communications and marketing. We would like to modify the content within the template by placing different images in copy within the frame.

We're looking for a consistent theme, but a few different layouts of the template to allow us to feature different products / messages. I have attached a PDF of some wire frames to convey our desired result. Please do not use the wire frame as is, place markers have not been sized to our most commonly used image sizes.

Core image sizes (products):

Most of our item images are mounted on a white background, and they are in three core sizes: (examples attached)
- 800 x 800
- 350 x 350
- 150 x 150

The templates should allow us to change the feature items and copy without too much difficulty. We have limited HTML/CSS knowledge, but enough to swap image references and copy. That being said, we're looking for a template / design that allows us to switch image reference links and write different copy within the design template. We would like to keep all background, header, and footer elements the same and consistent...the content within is what we hope to manipulate for different audiences and messaging.

We're looking to develop this type of theme / color scheme / feel - https://ravenmark.filedock.net/s/kp4tz7qmh2x9vbn3rcaf

Bottom line: We're looking for creative modification and usable email templates to commence a more pro-active marketing presence.

This design / theme will be the basis for all digital and traditional media moving forward. We're looking to deliver consistent messaging, theme, and branding across all of our efforts, and raise the bar on production value across the board.

Core catalog assets, design examples (some of them are bad), and item images are here - https://ravenmark.filedock.net/s/q5m2wd8ky7zt3hpsn4ux

Website (no judgements) - www.ravenmarkgoods.example

We're looking for this to be the start of several design based initiatives, including website redesign that is in the planning stages.

We look forward to improving our image with you!

Project Deadline Extended
Reason: We've decided to extend the deadline out based on the feedback from some designers, this project will close on November 12th. Thank you for the feedback, we're looking forward to seeing the results!

Thank you for your submissions, we greatly appreciate your ideas and efforts to capture our objectives. Several of you have submitted good designs, it's been challenging to decide on just one for this. We are looking to work with some of you moving forward on other projects, so even if you didn't win this particular project, please know we're going to keep the dialogue / opportunities coming. Thank you again, providing a framework and connecting us with talented people like all of you is where I consider the true value of this service. This was our first time utilizing the service, I appreciate the value for the opportunities it provides to both parties. Cheers! Lou Brackwell

Target Market(s)

Our target market is North American professional sales and marketing people. Ages 25 - 50.

Industry/Entity Type

Communications

```html
<!DOCTYPE html>
<html lang="en">
<head>
<meta charset="utf-8">
<title>Ravenmark Newsletter</title>
<link rel="stylesheet" href="https://fonts.googleapis.com/css2?family=Arimo:wght@400&family=Oswald:wght@500;700&family=Open+Sans:wght@400;600;700&display=swap">
<style>
  :root {
    --brand-blue: #2a5fb0;
    --deep-blue: #1d4f9a;
    --sky-blue: #4f86cf;
    --pale-blue: #e3ecf6;
    --stripe: #dbe5f0;
    --brand-red: #e0242a;
    --ink: #3c3c3c;
    --soft-ink: #555;
    --paper: #ffffff;
    --canvas-bg: #f5f7fa;
  }
  html, body { margin: 0; padding: 0; overflow: hidden; }
  body { background: var(--canvas-bg); }
  .newsletter {
    position: relative; width: 777px; height: 1200px; overflow: hidden;
    background: var(--paper); font-family: "Arimo", Arial, sans-serif; color: var(--ink);
  }
  .masthead {
    position: absolute; left: 0; top: 0; width: 777px; height: 80px;
    background: linear-gradient(90deg, #ffffff 0%, #c7d8ee 30%, var(--sky-blue) 70%, var(--brand-blue) 100%);
  }
  .brand-name {
    position: absolute; left: 26px; top: 16px; display: flex; align-items: center; gap: 10px;
    font-family: "Oswald", sans-serif; font-weight: 700; font-size: 40px; line-height: 1; color: #1a1a1a;
  }
  .brand-dot { width: 18px; height: 18px; border-radius: 50%; background: var(--brand-red); flex: none; }
  .rush-badge {
    position: absolute; right: 24px; top: 22px; font-family: "Oswald", sans-serif; font-weight: 700;
    font-size: 24px; color: #fff; letter-spacing: 1px;
  }
  .rush-badge .rush-hours { color: #fff; background: var(--brand-red); padding: 0 5px; border-radius: 4px; margin: 0 4px; }
  .stripe-band {
    position: absolute; left: 0; width: 777px;
    background: repeating-linear-gradient(-60deg, var(--stripe) 0 12px, var(--paper) 12px 24px);
  }
  .stripe-top { top: 80px; height: 40px; }
  .stripe-mid { top: 486px; height: 52px; }
  .card {
    position: absolute; background: var(--paper);
    box-shadow: 0 3px 6px rgba(0,0,0,.18);
  }
  .feature-card { left: 19px; top: 120px; width: 387px; height: 390px; overflow: hidden; }
  .product-photo { position: absolute; }
  .feature-photo { left: 0; top: 0; width: 387px; height: 390px; background: radial-gradient(circle at 55% 40%, #2b2b2b 0 28%, #9fd54a 29% 40%, #f4f4f4 60%); }
  .new-ribbon {
    position: absolute; left: -40px; top: 30px; width: 170px; height: 34px; background: var(--brand-red);
    transform: rotate(-45deg); color: #fff; font-family: "Oswald", sans-serif; font-weight: 500;
    font-size: 24px; text-align: center; line-height: 34px; letter-spacing: 1px;
  }
  .feature-copy { position: absolute; left: 428px; top: 165px; width: 325px; }
  .feature-title {
    margin: 0 0 22px; font-family: "Open Sans", sans-serif; font-weight: 400; font-size: 23px;
    line-height: 28px; text-transform: uppercase; color: var(--brand-blue);
  }
  .feature-title .accent { display: block; color: var(--brand-red); }
  .feature-copy p { margin: 0 0 20px; font-size: 13px; line-height: 17px; color: var(--soft-ink); }
  .product-card { top: 571px; width: 342px; height: 418px; }
  .card-left { left: 29px; }
  .card-right { left: 406px; }
  .product-card .product-photo { left: 0; top: 0; width: 342px; height: 284px; }
  .photo-stationery { background: linear-gradient(160deg, #f4f6fa 0%, #3a6fc4 35%, #f3f3f3 60%, #e85a4f 85%, #f7f7f7 100%); }
  .photo-drawstring { background: linear-gradient(120deg, #6b3fb0 0%, #f1e230 40%, #f5e640 60%, #99d13d 85%, #ffffff 100%); }
  .product-card p {
    position: absolute; left: 30px; right: 30px; top: 298px; margin: 0; text-align: center;
    font-size: 13px; line-height: 17px; color: var(--soft-ink);
  }
  .plane-art {
    position: absolute; left: 610px; top: 1040px; width: 160px; height: 86px; z-index: 1;
    background: radial-gradient(ellipse at 50% 60%, #f2f2f2 0 35%, #d9dde3 55%, rgba(255,255,255,0) 72%);
  }
  .contact-strip {
    position: absolute; left: 44px; top: 1062px; z-index: 2;
    font-family: "Open Sans", sans-serif; color: var(--brand-blue); white-space: nowrap;
  }
  .contact-strip .serve { font-size: 17px; line-height: 22px; margin: 0; }
  .contact-strip .serve strong { font-weight: 700; margin-left: 16px; }
  .contact-strip .reach { font-size: 14px; line-height: 20px; margin: 2px 0 0; }
  .contact-strip .reach strong { font-weight: 700; }
  .footer-bar {
    position: absolute; left: 0; top: 1126px; width: 777px; height: 74px;
    background: linear-gradient(90deg, var(--deep-blue), var(--sky-blue) 60%, var(--brand-blue));
  }
  .tagline {
    position: absolute; font-family: "Oswald", sans-serif; font-weight: 500; color: #fff;
    font-size: 19px; line-height: 23px; text-transform: uppercase; white-space: nowrap;
  }
  .tagline-start { left: 16px; top: 8px; }
  .tagline-end { left: 250px; top: 13px; }
  .footer-brand {
    position: absolute; left: 104px; top: 36px; display: flex; align-items: center; gap: 6px;
    font-family: "Oswald", sans-serif; font-weight: 700; font-size: 20px; color: #1a1a1a;
    background: #fff; padding: 0 8px; border-radius: 4px; line-height: 28px; white-space: nowrap;
  }
  .footer-brand .brand-dot { width: 10px; height: 10px; }
  .social-links { position: absolute; left: 418px; top: 19px; display: flex; gap: 15px; margin: 0; padding: 0; list-style: none; }
  .social-links li { width: 36px; height: 36px; }
  .social-a { background: #3b5a99; }
  .social-b { background: #2aa8e0; }
  .social-c { background: #1c73b0; }
  .social-d { background: #dd4a38; }
  .social-e { background: #cf2030; }
  .social-f { background: #c4302b; }
  .social-g { background: #e53892; }
</style>
</head>
<body>
<main class="newsletter">
  <header class="masthead" role="img" aria-label="Blue header band with faint world map">
    <div class="brand-name"><span>Ravenmark</span><span class="brand-dot"></span></div>
    <div class="rush-badge">FREE<span class="rush-hours">24 HOUR</span>RUSH</div>
  </header>
  <div class="stripe-band stripe-top"></div>
  <div class="stripe-band stripe-mid"></div>

  <section class="card feature-card">
    <div class="product-photo feature-photo" role="img" aria-label="Black and lime drawstring backpack with printed logo, plus four colour variants below"></div>
    <div class="new-ribbon">NEW</div>
  </section>

  <article class="feature-copy">
    <h1 class="feature-title">Lorem ipsum dolor<span class="accent">cenafe tyuide</span></h1>
    <p>Lorem ipsum dolor sit amet, consectetur adipiscing elit. Sed dictum in turpis in tempor. Donec at tempus venenatis in eu enim. In hac habitasse platea dictumst. Pellentesque consectetur iaculis nulla, sed ultricies mauris gravida ut. Vivamus quis facilisis risus, at feugiat dolor. Ut vitae mattis libero.</p>
    <p>Vivamus mauris urna, dignissim vel dictum sit amet, tempor nec lacus. Mauris porttitor sem nec risus feugiat, sed tincidunt dui facilisis. Pellentesque gravida.</p>
  </article>

  <section class="card product-card card-left">
    <div class="product-photo photo-stationery" role="img" aria-label="Translucent blue and red desk cases with sticky notes and paper clips"></div>
    <p>Nulla placerat, felis at tempus pellentesque, libero velit varius nisl, nec consequat ex dolor et malesuada fames ac ante ipsum primis in faucibus. Etiam posuere, felis sit amet dignissim rhoncus, mauris purus vehicula saugue.</p>
  </section>

  <section class="card product-card card-right">
    <div class="product-photo photo-drawstring" role="img" aria-label="Yellow printed drawstring bag with purple and green bags behind and a row of colour swatches"></div>
    <p>Vivamus mauris urna, dignissim vel dictum sit amet, tempor nec lacus. Mauris porttitor sem nec risus feugiat, sed tincidunt dui facilisis. Pellentesque gravida.</p>
  </section>

  <div class="plane-art" role="img" aria-label="White and red passenger jet flying to the left"></div>
  <div class="contact-strip">
    <p class="serve">We are ready to serve you <strong>visit www.ravenmarkgoods.example</strong></p>
    <p class="reach">To view our product range and contact us at <strong>info@ravenmarkgoods.example</strong></p>
  </div>

  <footer class="footer-bar">
    <div class="tagline tagline-start">Come fly with</div>
    <div class="footer-brand"><span>Ravenmark</span><span class="brand-dot"></span></div>
    <div class="tagline tagline-end">And watch your<br>business take off</div>
    <ul class="social-links" aria-label="Social links">
      <li class="social-a"></li><li class="social-b"></li><li class="social-c"></li><li class="social-d"></li><li class="social-e"></li><li class="social-f"></li><li class="social-g"></li>
    </ul>
  </footer>
</main>
</body>
</html>
```